Landscape Company in need of logo and business card update. Current logo file is attached.

I need a business card design for a Woman Owned Landscape business in Kansas City. I do Native plant installation and maintenance as well as mowing, chemical applications and residential and commercial landscaping.
My colors are navy, green and white.
I currently have a logo that can be used or you can redesign it.

Target Market(s)

Residential and commercial

Industry/Entity Type

Landscape

Contact Information for Business Card

On back of current card it lists what I do and website:
BMP/Raingarden Maintenance and Installation, Certified Chemical Applicator for Trees, shrubs, and turf; Landscape Design and Installation for residential and commercial.

Logo Text

Birchwell Landscape Partners, LLC

Font styles to use
Other font styles liked:
• See current font on logo examples

Requirements
Must have
• Phone number: 913-555-0182
• Website: www.birchwellyards.example
• Colors: Navy, Green, white
• Email: birchwellyards@mailbox.example
• Address: PO BOX 417208 Shawnee, KS 66286
• Name of Person: Marlene Kozik, owner

```html
<!DOCTYPE html>
<html lang="en">
<head>
<meta charset="utf-8">
<title>Birchwell Landscape Partners – Business Card</title>
<link rel="stylesheet" href="https://fonts.googleapis.com/css2?family=Source+Sans+3:wght@400&family=Arimo:wght@400&family=Montserrat:wght@400&display=swap">
<style>
  :root {
    --backdrop: #dcdddd;
    --card: #ffffff;
    --leaf: #8cab1c;
    --leaf-deep: #6f8f0e;
    --lime: #b4d22a;
    --moss: #4f7a0c;
  }
  * { box-sizing: border-box; margin: 0; padding: 0; }
  html, body {
    width: 1200px; height: 788px; overflow: hidden;
    background: var(--backdrop);
  }
  .canvas { position: relative; width: 1200px; height: 788px; }

  .card {
    position: absolute;
    width: 430px; height: 278px;
    background: var(--card);
    overflow: hidden;
    box-shadow: 0 0 1px rgba(0,0,0,.15);
  }
  .card--front { left: 407px; top: 78px; }
  .card--back  { left: 405px; top: 379px; }

  .grass-photo { position: absolute; top: 0; bottom: 0; }
  .card--front .grass-photo {
    left: 0; right: 0;
    background:
      radial-gradient(ellipse 40px 140px at 312px 150px, rgba(190,225,60,.9), transparent 70%),
      radial-gradient(circle at 420px 40px, rgba(120,160,20,.7), transparent 40%),
      linear-gradient(to right, #ffffff 0%, #ffffff 36%, #eef6cf 46%, var(--lime) 62%, #97bf1d 78%, var(--moss) 100%);
  }
  .card--back .grass-photo {
    left: 0; right: 0;
    background:
      radial-gradient(ellipse 40px 140px at 110px 140px, rgba(190,225,60,.9), transparent 70%),
      radial-gradient(circle at 10px 240px, rgba(110,150,20,.7), transparent 40%),
      linear-gradient(to left, #ffffff 0%, #ffffff 40%, #eef6cf 52%, var(--lime) 66%, #97bf1d 82%, var(--moss) 100%);
  }

  .brand {
    position: absolute; left: 22px; top: 26px;
    display: flex; align-items: center; gap: 7px;
    font-family: "Source Sans 3", sans-serif;
    font-size: 13px; line-height: 1.15; letter-spacing: .5px;
    color: var(--leaf);
    text-transform: uppercase;
  }
  .brand__dot { width: 16px; height: 16px; border-radius: 50%; background: var(--leaf); flex: none; }

  .owner-name {
    position: absolute; left: 23px; top: 99px;
    font-family: "Source Sans 3", sans-serif;
    font-size: 41px; font-weight: 400;
    color: var(--leaf);
    white-space: nowrap;
  }
  .owner-title {
    position: absolute; left: 22px; top: 148px; width: 244px;
    display: flex; align-items: center; gap: 10px;
    font-family: "Montserrat", sans-serif;
    font-size: 12px; letter-spacing: 1.6px;
    color: var(--leaf);
  }
  .owner-title::before, .owner-title::after {
    content: ""; flex: 1; height: 1px; background: var(--leaf);
  }

  .contact {
    position: absolute; left: 22px; top: 206px;
    font-family: "Arimo", sans-serif;
    color: var(--leaf);
  }
  .contact__phone { font-size: 15px; letter-spacing: .8px; margin-bottom: 3px; }
  .contact__line { font-size: 9px; line-height: 12px; }

  .services {
    position: absolute; left: 210px; top: 82px;
    list-style: none;
    font-family: "Source Sans 3", sans-serif;
    font-size: 12.5px; line-height: 16px;
    color: var(--leaf);
  }
  .services li { display: flex; gap: 12px; margin-bottom: 9px; }
  .services li::before {
    content: ""; width: 7px; height: 7px; margin-top: 5px; flex: none;
    border-radius: 50%; background: var(--leaf);
  }
</style>
</head>
<body>
<main class="canvas">
  <section class="card card--front" aria-label="Business card front">
    <div class="grass-photo" role="img" aria-label="Close-up photo of green grass blades with water droplets"></div>
    <div class="brand"><span class="brand__dot"></span><span>Birchwell Landscape<br>Partners, LLC</span></div>
    <h1 class="owner-name">Marlene Kozik</h1>
    <p class="owner-title">OWNER</p>
    <div class="contact">
      <p class="contact__phone">913-555-0182</p>
      <p class="contact__line">PO BOX 417208 Shawnee, KS 66286</p>
      <p class="contact__line">www.birchwellyards.example</p>
      <p class="contact__line">birchwellyards@mailbox.example</p>
    </div>
  </section>

  <section class="card card--back" aria-label="Business card back">
    <div class="grass-photo" role="img" aria-label="Close-up photo of a grass blade with dew drops"></div>
    <ul class="services">
      <li><span>BMP/Raingarden<br>Maintenance and Installation</span></li>
      <li><span>Certified Chemical Applicator<br>for Trees, shrubs, and turf</span></li>
      <li><span>Landscape Design and Installation<br>for residential and commercial</span></li>
    </ul>
  </section>
</main>
</body>
</html>
```